Name Card Design

Looking to create a card for my business. I am a personal stylist, my business is clothes, shoes and everything to do with looking fashion forward. I help people achieve the most polished look with cloths and grooming. I would like my card to be a reflection of my qualities which are: poise, elegance, creativity and fairness.
Things I like a simple yet expensive looking, sometimes less simple but highly creative and different catches my eye. For instance I saw a card with lace trimming at the bottom, it made me think about the business that person was in. I don't like childish designs with butterflies, trees, flowers, etc.
Here is my site www.Marta-Vosel.example for your perusal

On the card it should have the following info
Marta Vosel
personal stylist
www.Marta-Vosel.example
(+65) 482-30857
Facebook page: Ringthelook

Back of the card:
Wardrobe weeding
Personal shopping
Style consultation

Target Market(s)

mostly working women

Industry/Entity Type

Fashion

Font styles to use
Serif
Sans Serif

Requirements
Should not have
• butterflies, flowers, feathers, etc

```html
<!DOCTYPE html>
<html lang="en">
<head>
<meta charset="utf-8">
<title>Marta Vosel — Personal Stylist Business Card</title>
<link rel="stylesheet" href="https://fonts.googleapis.com/css2?family=Lato:wght@400&family=Petit+Formal+Script&display=swap">
<style>
  :root {
    --stage: #4b4b4b;
    --powder-blue: #aee0f3;
    --ink: #000000;
    --paper-white: #ffffff;
    --trim-dark: #0a0a0a;
  }
  * { margin: 0; padding: 0; box-sizing: border-box; }
  html, body { width: 1200px; height: 1000px; overflow: hidden; }
  body { background: var(--stage); position: relative; }

  .card {
    position: absolute;
    width: 620px;
    height: 363px;
    overflow: hidden;
    box-shadow: 0 2px 6px rgba(0,0,0,0.35);
  }

  /* Services side */
  .card--services { left: 131px; top: 119px; background: var(--powder-blue); }
  .services-list {
    position: absolute;
    left: 0; top: 128px;
    width: 598px;
    text-align: center;
    font-family: "Petit Formal Script", cursive;
    font-size: 23px;
    line-height: 43px;
    color: var(--ink);
  }
  .services-list__divider {
    font-family: "Lato", sans-serif;
    font-size: 26px;
    color: var(--ink);
  }
  .card--services .lace-trim {
    position: absolute; left: 0; bottom: 0;
    width: 100%; height: 57px;
    background: linear-gradient(180deg, var(--trim-dark) 0%, #1c2a30 100%);
  }

  /* Contact side */
  .card--contact { left: 425px; top: 524px; width: 618px; background: var(--ink); }
  .brand-name {
    position: absolute; left: 40px; top: 54px;
    font-family: "Lato", sans-serif;
    font-weight: 400;
    font-size: 38px;
    line-height: 46px;
    color: var(--paper-white);
  }
  .identity { position: absolute; left: 373px; top: 56px; font-family: "Lato", sans-serif; }
  .identity__name { font-size: 27px; color: var(--powder-blue); line-height: 34px; }
  .identity__role { font-size: 15px; color: var(--paper-white); line-height: 24px; }

  .contact-list {
    position: absolute; left: 378px; top: 161px;
    list-style: none;
    font-family: "Lato", sans-serif;
    font-size: 16px;
    color: var(--paper-white);
  }
  .contact-list li { display: flex; align-items: center; height: 26px; }
  .contact-list svg { width: 14px; height: 14px; margin-right: 10px; flex: none; }

  .card--contact .lace-trim {
    position: absolute; left: 0; bottom: 0;
    width: 100%; height: 57px;
    background: linear-gradient(180deg, var(--powder-blue) 0%, #8fc9de 100%);
  }
</style>
</head>
<body>

<section class="card card--services">
  <p class="services-list">Wardrobe Weeding <span class="services-list__divider">|</span> Personal Shopping<br>Style Consultation</p>
  <div class="lace-trim" role="img" aria-label="Scalloped lace trim border with small bow and blossom motifs"></div>
</section>

<section class="card card--contact">
  <div class="brand-name">Marta Vosel</div>

  <div class="identity">
    <div class="identity__name">Marta Vosel</div>
    <div class="identity__role">Personal Stylist</div>
  </div>

  <ul class="contact-list">
    <li>
      <svg viewBox="0 0 14 14" aria-hidden="true"><rect x="3.5" y="0.8" width="7" height="12.4" rx="1.2" fill="none" stroke="#fff" stroke-width="1.4"/><circle cx="7" cy="11" r="0.8" fill="#fff"/></svg>
      (+65) 482-30857
    </li>
    <li>
      <svg viewBox="0 0 14 14" aria-hidden="true"><rect x="1" y="3" width="12" height="8.5" fill="#fff"/><path d="M1 3 L7 8 L13 3" fill="none" stroke="#000" stroke-width="1.2"/></svg>
      stylist@marta-vosel.example
    </li>
    <li>
      <svg viewBox="0 0 14 14" aria-hidden="true"><circle cx="7" cy="7" r="5.8" fill="none" stroke="#fff" stroke-width="1.4"/><path d="M1.5 7 H12.5 M7 1.2 C4.5 4 4.5 10 7 12.8 M7 1.2 C9.5 4 9.5 10 7 12.8" fill="none" stroke="#fff" stroke-width="1"/></svg>
      www.Marta-Vosel.example
    </li>
    <li>
      <svg viewBox="0 0 14 14" aria-hidden="true"><circle cx="7" cy="7" r="5" fill="var(--powder-blue)"/></svg>
      Ringthelook
    </li>
  </ul>

  <div class="lace-trim" role="img" aria-label="Scalloped lace trim border with small bow and blossom motifs"></div>
</section>

</body>
</html>
```